Stationary and Logo Design Project

We need a full corporate logo and stationary design for our company Kivora5X. Kivora5X specializes in creating custom adult sex toys using CAD and 3D Printing technologies as part of the process. The companies tagline is "Your Pleasure, Your Way", though this is not required to be part of the logo.

We are looking for something sensual, romantic and sexy, but not something explicit and vulgar.

As the company will be targeting mid to high-end clientele tastefulness is very important to us - this is difficult when the service we are selling is sex but can be achieved.

What we are after:

1. Logo
2. Business Card Design
3. Letterhead Design
4. Email Signature Design

File Formats we require in colour, greyscale and Black and White:

1 .AI
2 .EPS
3 .TIF
4 .PDF
5 .PNG (300 dpi)
6 .JPG (300 dpi)
7 .GIF (300 dpi)

Target Market(s)

Adults between the ages of 21 and 50 (Predominantly female but not limited to) who like there sex toys and want a custom job.

Industry/Entity Type

Adult

Requirements
Must have
• As we are planning on advertising in the future make sure the art is suitable for print advertising.
Nice to have
• The tagline "Your Pleasure, Your Way" on the business card, letterhead and email signature.
Should not have
• Explicit/vulgar illustrations.

"Clip-Art" should not be used.

```html
<!DOCTYPE html>
<html lang="en">
<head>
<meta charset="utf-8">
<title>Kivora5X Business Card</title>
<link rel="stylesheet" href="https://fonts.googleapis.com/css2?family=Roboto+Condensed:wght@400;700&display=swap">
<style>
  :root {
    --paper: #ffffff;
    --card-black: #000000;
    --magenta: #d6186e;
    --rose: #e0628f;
    --plum: #5e2468;
    --deep-plum: #3f0c47;
    --ink-light: #ffffff;
    --card-shadow: rgba(0, 0, 0, 0.18);
  }
  html, body {
    margin: 0;
    padding: 0;
    width: 1200px;
    height: 901px;
    overflow: hidden;
    background: var(--paper);
    font-family: "Roboto Condensed", "Arial Narrow", sans-serif;
  }
  .canvas {
    position: relative;
    width: 1200px;
    height: 901px;
  }
  .card {
    position: absolute;
    left: 265px;
    width: 681px;
    height: 343px;
    border-radius: 28px;
    background: var(--card-black);
    overflow: hidden;
    box-shadow: 0 8px 14px var(--card-shadow);
  }
  .card--front { top: 71px; }
  .card--back { top: 481px; }

  .front-artwork {
    position: absolute;
    inset: 0;
    background: linear-gradient(180deg, var(--rose) 0%, var(--magenta) 35%, var(--plum) 80%, var(--deep-plum) 100%);
    clip-path: polygon(0 22%, 45% 0, 100% 0, 100% 74%, 60% 100%, 10% 100%, 0 70%);
  }
  .front-brand {
    position: absolute;
    right: 58px;
    top: 222px;
    font-size: 46px;
    font-weight: 700;
    color: var(--ink-light);
    letter-spacing: 0.5px;
  }

  .contact {
    position: absolute;
    left: 37px;
    top: 98px;
    color: var(--ink-light);
  }
  .contact__name {
    margin: 0;
    font-size: 22px;
    font-weight: 400;
    line-height: 1;
  }
  .contact__role {
    margin: 7px 0 0;
    font-size: 15px;
    color: var(--magenta);
    line-height: 1;
  }
  .contact__lines {
    margin: 35px 0 0;
    font-size: 19px;
    line-height: 27px;
  }
  .contact__lines + .contact__lines { margin-top: 29px; }

  .back-brand {
    position: absolute;
    left: 600px;
    top: 170px;
    transform: translate(-50%, -50%) rotate(90deg);
    font-size: 34px;
    font-weight: 700;
    color: var(--magenta);
    white-space: nowrap;
  }
</style>
</head>
<body>
  <main class="canvas">
    <section class="card card--front" aria-label="Business card front">
      <div class="front-artwork" role="img" aria-label="Large stylised brand lettering decoration in pink and plum"></div>
      <div class="front-brand">Kivora5X</div>
    </section>

    <section class="card card--back" aria-label="Business card back">
      <div class="contact">
        <p class="contact__name">Mara Lindqvist</p>
        <p class="contact__role">Director</p>
        <p class="contact__lines">t. +61 03 5550 1234<br>f. +61 03 5550 4321</p>
        <p class="contact__lines">mara@kivora5x.com<br>www.kivora5x.com</p>
      </div>
      <div class="back-brand">Kivora5X</div>
    </section>
  </main>
</body>
</html>
```